Brochure Design Project

We require a great design for a brochure that we will be giving to people who are interested in buying one of our franchises.
From this brochure they will need to get the feel of a succesful business that they would love to be a part of

Please also include the title
Become Part of a National Sign Manufacturing Company

Hi Everyone
Does anyone have any designs that they are adding because we will be making our descision in approx an hour

Thank you

Industry/Entity Type

Business

Requirements
Must have
• This brochure must be 2 page A4 (front and back)
can be either portrait or landscape orientation (which ever works best with the design)
Must have our logo and colours
Must include all the information provided in the Word Document
Nice to have
• Can include images if it works with the design
can use either stock images of profesionals or see our website
www.vorlix.com.au for some images

```html
<!DOCTYPE html>
<html lang="en">
<head>
<meta charset="utf-8">
<title>Vorlix Franchise Brochure</title>
<link href="https://fonts.googleapis.com/css2?family=Jost:wght@400;500;600&family=Arimo:wght@400;700&display=swap" rel="stylesheet">
<style>
  :root {
    --stage: #58595b;
    --blue-deep: #0b4a99;
    --blue-mid: #1565b8;
    --blue-light: #3d95dc;
    --blue-pale: #bfe3fb;
    --heading: #1f4e9a;
    --body: #555a60;
    --brand: #26466f;
    --white: #ffffff;
  }
  * { box-sizing: border-box; margin: 0; padding: 0; }
  html, body { width: 1200px; height: 867px; overflow: hidden; }
  body { background: var(--stage); position: relative; font-family: 'Arimo', Arial, sans-serif; }

  .page { position: absolute; top: 27px; width: 552px; height: 781px; border: 1px solid #cfd6df; overflow: hidden; }
  .page--front {
    left: 38px;
    background: radial-gradient(ellipse at 50% 40%, var(--blue-light) 0%, var(--blue-mid) 50%, var(--blue-deep) 100%);
  }
  .page--back { left: 610px; background: var(--white); }

  /* front */
  .brand {
    position: absolute; top: 76px; left: 0; width: 100%; text-align: center;
    font-family: 'Jost', sans-serif; font-weight: 600; font-size: 56px; letter-spacing: 4px;
    color: var(--brand);
  }
  .headline {
    position: absolute; top: 152px; left: 60px; width: 432px; text-align: center;
    font-family: 'Jost', sans-serif; font-weight: 500; font-size: 17px; line-height: 22px;
    color: var(--white);
  }
  .hero {
    position: absolute; top: 205px; left: 24px; width: 528px; height: 380px;
    background:
      radial-gradient(ellipse 42% 48% at 50% 52%, rgba(150,205,245,.85) 0%, rgba(90,165,230,.55) 55%, rgba(40,120,205,0) 100%),
      radial-gradient(ellipse 60% 22% at 55% 85%, rgba(215,240,255,.75) 0%, rgba(150,210,250,.35) 55%, rgba(40,120,205,0) 100%);
  }
  .tagline {
    position: absolute; left: 131px; top: 636px;
    font-family: 'Jost', sans-serif; font-weight: 400; font-size: 32px; line-height: 46px;
    color: var(--white);
  }

  /* back */
  .section { position: absolute; }
  .section--left { left: 30px; width: 270px; }
  .section--right { left: 317px; width: 198px; }
  .section-title { font-weight: 700; font-size: 11.5px; color: var(--heading); margin: 0 0 9px; }
  .section-text { font-size: 8.4px; line-height: 10.2px; color: var(--body); text-align: justify; }
  .section--right .section-text { font-size: 8.8px; line-height: 11.2px; }
  .section-text p { margin: 0; }

  .s-opportunity { top: 25px; }
  .s-clients     { top: 156px; }
  .s-pricing     { top: 230px; }
  .s-consistency { top: 328px; }
  .s-ease        { top: 448px; }
  .s-get         { top: 25px; }
  .s-need        { top: 322px; }

  .offer {
    position: absolute; left: 317px; top: 662px; width: 185px; list-style: none;
    font-weight: 700; font-size: 12.5px; line-height: 15px; color: var(--heading);
  }
  .offer li { padding-left: 10px; text-indent: -10px; }
  .contact-band {
    position: absolute; left: 0; top: 720px; width: 100%; height: 49px;
    background: linear-gradient(90deg, var(--blue-deep), var(--blue-mid));
    color: var(--white); text-align: center; font-weight: 700; font-size: 11.5px; line-height: 18px; padding-top: 6px;
  }
  .page-label { position: absolute; top: 818px; font-size: 20px; color: var(--white); }
  .page-label--front { left: 283px; }
  .page-label--back { left: 845px; }
</style>
</head>
<body>
  <section class="page page--front">
    <div class="brand">VORLIX</div>
    <h1 class="headline">Become Part of a National Sign Manufacturing Company</h1>
    <div class="hero" role="img" aria-label="Businessman raising both fists in celebration, with swirling light-blue wing shapes, waves and bubbles behind him"></div>
    <p class="tagline">Providing profitable<br>solutions for your<br>business success.</p>
  </section>

  <section class="page page--back">
    <div class="section section--left s-opportunity">
      <h2 class="section-title">Opportunity</h2>
      <p class="section-text">An exciting opportunity exists for 7 people to become part of a national sign manufacturing company servicing big name clientele on a national scale. A successful applicant will receive their own State territory branch to operate a sign manufacturing and installation service to our existing clientele. This will be strictly limited to 1 franchise sold per state and if the operator chooses or feels they can better service our clients with multiple outlets within their state then they are at liberty to do so without any further fees incurred.</p>
    </div>
    <div class="section section--left s-clients">
      <h2 class="section-title">Our Clients</h2>
      <p class="section-text">Our clients are franchises, shopfitters, architects, designers, brokers, multisite organisations and anyone who is ordering signs on a regular basis. We have targeted this clientele for the obvious reasons of continuous work and in return our clients receive:</p>
    </div>
    <div class="section section--left s-pricing">
      <h2 class="section-title">Competitive Pricing</h2>
      <p class="section-text">The reason you will be able to offer competitive pricing is because you will not have to waste time and money on things like in-house design, advertising, sales reps high exposure sales locations and the list goes on<br>All of these savings are passed on to our clients and for this reason we remain number 1 choice time and time again.</p>
    </div>
    <div class="section section--left s-consistency">
      <h2 class="section-title">Consistency and Reliability</h2>
      <p class="section-text">We have systems in place to ensure consistency and reliability across branches by adhering to a minimum standards and code of conduct policy which our customers can view at any time which outlines things such as standard material specifications, warranty periods, standard turnaround times, standard pricing schedules and more, to add to all this the operating systems and software we use ensure reliable and familiar interaction with our clients no matter which branch they are dealing with.</p>
    </div>
    <div class="section section--left s-ease">
      <h2 class="section-title">Ease of Use</h2>
      <p class="section-text">Just think about it one of the roles of an operations manager of a large company is the organisation and ordering all of the signage requirements for 45 different locations across Australia. Whilst at one of the locations in NSW he notices that the front window graphics have been damaged by graffiti, He calls the NSW Vorlix branch and begins the process of ordering some replacement window graphics and chooses to freshen up the graphics with some new designs that had been recently added to the brands new style guide, now he already knows that he is getting a quality product that has been specified in the minimum standards and code of conduct policy and he already knows the cost of the product because the pricing structure has also been outlined he knows that the branch has access to the customers data base with style guide so he knows they have the artwork files plus he knows that the colours will be correct because all that info is in the customers file, so in other words he know how easy it is to order from the Vorlix branch. Then one week later he is in Victoria visiting another one of the 45 locations and would you believe he notices that yet again the windows have been vandalised and yes another opportunity to refresh the images so off course he call the Vorlix VIC office and begins the process again and all he has to do is say we want the graphics exactly the same as the ones done 2 weeks ago at the other location, Easy</p>
    </div>

    <div class="section section--right s-get">
      <h2 class="section-title">What do you get</h2>
      <div class="section-text">
        <p>•You will receive your own State to operate and fulfil all orders within that state</p>
        <p>•You can have as many manufacturing facilities you feel are needed to efficiently operate within your state and the best part is that you can grow this over time.</p>
        <p>•Operating Procedures and software including quoting systems and pricing structure</p>
        <p>•Pre-existing clientele we have been operating since 2006 and have a national network that is growing by the day</p>
        <p>•National website and number</p>
        <p>•Marketing and new client introduction</p>
        <p>•Benefits of being part of a national team that is capable of servicing national clients that would not be possible to service otherwise</p>
        <p>•The benefits of this business are growing daily and we have not even scratched the surface of its full potential more and more clients are realising just how much they can benefit from using our services.</p>
      </div>
    </div>
    <div class="section section--right s-need">
      <h2 class="section-title">What you need</h2>
      <div class="section-text">
        <p>To be successful in ensuring your position within our team you will need to have had experience within the signage industry, have great communication skills and have a good positive attitude towards owning and running a successful business. Under no circumstances can you own or be in any way affiliated with another sign company and own a Vorlix branch you can however apply if you are closing or exiting (or intending to exit if successful)</p>
        <p>Some working capital will be needed and this will obviously vary depending on the size of the initial manufacturing setup but a minimum of $20,000 would be advised.</p>
        <p>A Once off purchase price of your territory will cost $45,000.</p>
        <p>A suitable place of business, at a minimum this will consist of small office area and ideally 200sqm or more of workshop space.</p>
        <p>There is various machinery and equipment required and leasing options will be available Costs</p>
      </div>
    </div>

    <ul class="offer">
      <li>• $45,000 once off purchase price for your territory</li>
      <li>• 7% of sales</li>
    </ul>

    <div class="contact-band">
      For more information or to apply call<br>
      1300 555 019 | Email: accounts@vorlix.com.au | www.vorlix.com.au
    </div>
  </section>

  <span class="page-label page-label--front">Front</span>
  <span class="page-label page-label--back">Back</span>
</body>
</html>
```